Health and Wellness. I am an energetic, but not over the top, Certified Personal Trainer and Nutriti

I need a flyer, 8.5 x 11, representing my company to be displayed in a Doctor's office that specializes in Pain Medicine. Most, if not all, of these clients experience pain or have some chronic diseases such as high blood pressure, high cholesterol, back pain, joint pain, etc. So the flyer should convey that exercise and nutrition reduce/relieves pain and references some of these ailments. Ideally, the flyer should depict an overweight person exercising with a content, or somewhat content or smiling expression on their face in some part of the flyer. My services cover nutrition and include personal training to where I Ideally train people in their home, equipment permitting, or outside in our local Floridian Parks, and sometimes beaches. This flyer will be in a display case, and the bottom right 8.5 x5 cm will need to be blank, or allow for me to input the back of my business car into it, as I'll have business cards readily available in front of the flyer to be taken. I've included some versions of my logos to be added to the flyer. The other picture is of the flyer holder, with business card area, that this flyer will be presented in. Finally, I've attached a pic of what the back of my business card looks like to be input into that bottom right hand corner. You'll be able to see the area in the bottom right that will display my business cards.
Target Market(s)
People looking for weight loss through Nutrition and Fitness. Those looking to relieve joint and/or back pain or those with Chronic diseases such as high blood pressure, high cholesterol, etc.
Industry/Entity Type
Doctor
Requirements
Must have
- Resemble my Logo's color scheme: Red, Teal, and Grey. Some type of photo of an overweight or slightly overweight person exercising.

```html
<!DOCTYPE html>
<html lang="en">
<head>
<meta charset="utf-8">
<title>Bergman's Fitness – Natural Blood Pressure Control</title>
<link href="https://fonts.googleapis.com/css2?family=Exo+2:wght@400;500&family=Roboto+Condensed:wght@300;400;700&family=Montserrat:wght@700&display=swap" rel="stylesheet">
<style>
  :root {
    --red: #ef4b52;
    --ink: #1b1b1b;
    --charcoal: #2a2a2a;
    --grey: #5b5b5b;
    --paper: #ffffff;
    --mist: #f1f1f1;
    --backdrop: #e9e6e1;
  }
  * { margin: 0; padding: 0; box-sizing: border-box; }
  html, body { width: 1038px; height: 1200px; overflow: hidden; background: var(--backdrop); }
  .flyer {
    position: absolute; left: 55px; top: 0;
    width: 865px; height: 1118px;
    transform: scale(1.0733); transform-origin: 0 0;
    background: var(--paper); overflow: hidden;
    font-family: "Roboto Condensed", sans-serif;
  }
  .shapes { position: absolute; inset: 0; }
  .brand {
    position: absolute; left: 28px; top: 150px;
    display: flex; align-items: center; gap: 10px;
    font-family: "Montserrat", sans-serif; font-weight: 700;
    font-size: 26px; letter-spacing: 1px; color: var(--grey);
  }
  .brand .dot { width: 22px; height: 22px; border-radius: 50%; background: var(--red); }
  .headline {
    position: absolute; left: 27px; top: 368px;
    font-family: "Exo 2", sans-serif; font-weight: 500; line-height: 1;
    letter-spacing: 2px;
  }
  .headline .line-1 { display: block; font-size: 56px; color: var(--red); }
  .headline .line-2 { display: block; font-size: 47px; color: var(--paper); margin-top: 4px; }
  .services { position: absolute; right: 39px; top: 615px; text-align: right; }
  .services h2 { font-weight: 700; font-size: 31px; color: var(--ink); line-height: 1.1; }
  .services .places { font-weight: 300; font-size: 23px; color: var(--ink); line-height: 30px; margin-top: 6px; }
  .services .audience { font-weight: 700; font-size: 20px; color: var(--red); line-height: 26px; margin-top: 31px; }
  .services .conditions { font-weight: 400; font-size: 16px; color: var(--ink); line-height: 20.5px; margin-top: 4px; }
  .phone {
    position: absolute; left: 30px; top: 950px;
    display: flex; align-items: center; gap: 12px;
    font-family: "Exo 2", sans-serif; font-weight: 500; font-size: 58px; color: var(--red); line-height: 1;
  }
  .website {
    position: absolute; left: 33px; top: 1010px;
    font-size: 20px; letter-spacing: 8.4px; color: var(--ink);
  }
  .contact-bar {
    position: absolute; left: 28px; top: 1072px;
    display: flex; align-items: center; gap: 10px;
    font-size: 17px; color: var(--paper);
  }
  .contact-bar .divider { margin: 0 26px; color: #cfcfcf; }
  .contact-bar .square { width: 14px; height: 14px; background: var(--red); }
</style>
</head>
<body>
<main class="flyer">
  <svg class="shapes" width="865" height="1118" viewBox="0 0 865 1118">
    <defs>
      <linearGradient id="parkTone" x1="0" y1="0" x2="1" y2="1">
        <stop offset="0" stop-color="#6f8a4c"/>
        <stop offset="0.5" stop-color="#4c5f3a"/>
        <stop offset="1" stop-color="#7c7a70"/>
      </linearGradient>
      <linearGradient id="gymTone" x1="0" y1="0" x2="1" y2="1">
        <stop offset="0" stop-color="#8a8a8a"/>
        <stop offset="1" stop-color="#2e2e2e"/>
      </linearGradient>
      <linearGradient id="cornerTone" x1="0" y1="0" x2="1" y2="0">
        <stop offset="0" stop-color="#5a5a5a"/>
        <stop offset="1" stop-color="#111"/>
      </linearGradient>
      <linearGradient id="softGym" x1="0" y1="0" x2="1" y2="0">
        <stop offset="0" stop-color="#e3e3e3"/>
        <stop offset="1" stop-color="#fbfbfb"/>
      </linearGradient>
    </defs>
    <!-- top outdoor training photo -->
    <rect class="photo-park" x="0" y="0" width="865" height="561" fill="url(#parkTone)" role="img" aria-label="Photo of a woman and a man doing push-up exercises at an outdoor park fitness station"/>
    <polygon points="0,273 865,455 865,561 0,561" fill="#1a1a1a" opacity="0.92"/>
    <polygon points="0,200 865,330 865,455 0,273" fill="#1a1a1a" opacity="0.45"/>
    <polygon points="0,0 225,0 405,200 0,273" fill="var(--paper)"/>
    <polygon points="705,561 865,461 865,561" fill="var(--red)"/>
    <!-- middle section -->
    <rect x="0" y="561" width="865" height="380" fill="url(#softGym)" role="img" aria-label="Faded background photo of a gym interior"/>
    <polygon points="140,561 172,561 632,941 600,941" fill="var(--ink)"/>
    <polygon class="photo-gym" points="0,561 140,561 600,941 0,941" fill="url(#gymTone)" role="img" aria-label="Black and white photo of a trainer guiding a woman lifting dumbbells"/>
    <!-- bottom section -->
    <polygon points="600,941 865,941 865,1118 700,1118" fill="url(#cornerTone)"/>
    <circle cx="793" cy="1011" r="48" fill="none" stroke="#3a3a3a" stroke-width="6"/>
    <polygon points="0,1043 720,1043 640,1118 0,1118" fill="var(--ink)"/>
    <polygon points="720,1043 740,1043 660,1118 640,1118" fill="var(--paper)"/>
    <polygon points="755,1043 828,1118 670,1118" fill="var(--red)"/>
  </svg>

  <div class="brand"><span class="dot"></span>BERGMAN'S FITNESS</div>

  <h1 class="headline">
    <span class="line-1">NATURAL BLOOD</span>
    <span class="line-2">PRESSURE CONTROL</span>
  </h1>

  <section class="services">
    <h2>FITNESS TRAINING IN</h2>
    <p class="places">Your Home, Online, Parks and Beaches,<br>Bride, Groom, and Bridal Party</p>
    <p class="audience">People looking for weight loss through<br>Nutrition and Fitness.</p>
    <p class="conditions">Those looking to relieve joint and/or back<br>pain or those with Chronic diseases<br>such as high blood pressure, high<br>cholesterol</p>
  </section>

  <div class="phone">
    <svg width="42" height="42" viewBox="0 0 24 24" aria-hidden="true"><path fill="var(--red)" d="M6.6 10.8a15.1 15.1 0 0 0 6.6 6.6l2.2-2.2c.3-.3.7-.4 1-.2 1.1.4 2.3.6 3.6.6.6 0 1 .4 1 1V20c0 .6-.4 1-1 1A17 17 0 0 1 3 4c0-.6.4-1 1-1h3.5c.6 0 1 .4 1 1 0 1.3.2 2.5.6 3.6.1.3 0 .7-.2 1z"/></svg>
    555-014-2297
  </div>
  <div class="website">www.bergmansfitness.com</div>

  <div class="contact-bar">
    <svg width="20" height="15" viewBox="0 0 20 15" aria-hidden="true"><rect width="20" height="15" rx="2" fill="var(--red)"/><path d="M1 2l9 6 9-6" fill="none" stroke="var(--ink)" stroke-width="1.8"/></svg>
    <span>bergmansfitness1@example.com</span>
    <span class="divider">|</span>
    <span class="square"></span>
    <span>@bergmansfitness</span>
  </div>
</main>
</body>
</html>
```